Online Art Gallery & Art Management Firm looking for a business card

I'm launching an online art gallery (paintings, photography, drawings, furniture, books, ...) where people can buy all types of art. It's a platform where young and unknown artists can showcase their oeuvre.

Additionally, the venture will act as my advising company for artists. I help them out with their business side of life and become their representative.

The company name: The Velmora House
Logo is attached

I'm looking for something very classy and upmarket.
Updates

Reason: Logo wasn't finished yet...

The design should include the following information: - Name: Pieter Drovensky - Title: Founder - Mobile: +32 (0) 485 613 204 - E-mail: pieter@velmora-house.net - Website www.velmora-house.net I prefer the have the logo (without website) on the one side and the information on the other. Best regards Pieter

Target Market(s)

Art buyers / art dealers / artists / middle class / upmarket /

Industry/Entity Type

Artists

Colors

Designer to choose colors to be used in the design.

Requirements
Must have
• Must communicate credibility, trust and integrity
Nice to have
• Something classy, chique
Should not have
• Nothing to artistic or creative

```html
<!DOCTYPE html>
<html lang="en">
<head>
<meta charset="utf-8">
<title>The Velmora House — Business Card</title>
<link rel="stylesheet" href="https://fonts.googleapis.com/css2?family=Open+Sans:wght@300;400&display=swap">
<style>
  :root {
    --backdrop: #3a3431;
    --card: #1c1f22;
    --ink: #e9eaeb;
    --ink-soft: #a9acaf;
    --shadow: rgba(0, 0, 0, 0.45);
  }
  * { margin: 0; padding: 0; box-sizing: border-box; }
  html, body {
    width: 1200px;
    height: 768px;
    overflow: hidden;
    background: var(--backdrop);
    font-family: "Open Sans", Arial, sans-serif;
    color: var(--ink);
  }
  .sheet {
    width: 1200px;
    height: 768px;
    display: flex;
    align-items: center;
    justify-content: center;
    gap: 40px;
  }
  .card {
    position: relative;
    width: 540px;
    height: 350px;
    background: var(--card);
    box-shadow: 0 10px 30px var(--shadow);
  }
  .wordmark {
    font-weight: 300;
    text-transform: uppercase;
    letter-spacing: 0.32em;
    color: var(--ink);
    white-space: nowrap;
  }
  .card--front .wordmark {
    position: absolute;
    top: 50%;
    left: 50%;
    transform: translate(-50%, -50%);
    font-size: 21px;
    color: var(--ink-soft);
  }
  .card--back .wordmark {
    position: absolute;
    top: 78px;
    right: 36px;
    font-size: 22px;
  }
  .contact {
    position: absolute;
    left: 170px;
    top: 142px;
  }
  .contact__name {
    font-size: 15px;
    font-weight: 300;
    color: var(--ink-soft);
    margin-left: 34px;
  }
  .contact__title {
    font-size: 12px;
    font-weight: 300;
    color: var(--ink-soft);
    margin-left: 34px;
    margin-bottom: 18px;
  }
  .contact__list {
    list-style: none;
    font-size: 14px;
    font-weight: 300;
    line-height: 1.5;
  }
  .contact__list li { display: flex; }
  .contact__label {
    width: 34px;
    color: var(--ink-soft);
  }
</style>
</head>
<body>
  <main class="sheet">
    <section class="card card--front" aria-label="Card front">
      <p class="wordmark">The Velmora House</p>
    </section>
    <section class="card card--back" aria-label="Card back">
      <p class="wordmark">The Velmora House</p>
      <div class="contact">
        <p class="contact__name">Pieter Drovensky</p>
        <p class="contact__title">Founder</p>
        <ul class="contact__list">
          <li><span class="contact__label">M</span>+32 (0) 485 613 204</li>
          <li><span class="contact__label">E</span>mail: pieter@velmora-house.net</li>
          <li><span class="contact__label">W</span>www.velmora-house.net</li>
        </ul>
      </div>
    </section>
  </main>
</body>
</html>
```